PowerPoint Design Project for Wellness Course

I run wellness courses and woul like a professional powerpoint presentation template that I can use for all of my projects.

It would need to have the following:

1. An opening title slide with the logo on it somewhere.

2. Every slide should display the logo (I will be changing the logo for different courses - so need to be able to change this or get you to make duplicates with the different logos - two of which are being created by pixelharbor right now) (I have attached two logos for you to use though)

3. A slide that has headings and bullet points.

3. A slide with heading, bullet points and pictures.

4. I would like the colours to be soft, it is meditation so nothing too loud. Blues would be nice as they are calming or any other calming colours.

I am attaching what the slides currently look like which was done by me and looks terrible, but will give you an idea of the things I put in the slides.

I want the designer to be creative :)

Target Market(s)

from 20's to 40's

Industry/Entity Type

Wellness

Requirements
Must have
• Must look professional. I want the bullet tabs to come into the presentation in a professional looking way. I don't want crazy lead ins with the bullets.

Must have the ability to easily change pictures and text for other projects.
Should not have
• Too many colours I do not want the colours to take away from the content.

```html
<!DOCTYPE html>
<html lang="en">
<head>
<meta charset="utf-8">
<title>Cocoa Calm – Slide Template</title>
<link rel="stylesheet" href="https://fonts.googleapis.com/css2?family=Carlito:wght@400;700&display=swap">
<style>
:root{
  --page:#ffffff;
  --mat-light:#f1e9da;
  --mat-mid:#e4d6bf;
  --mat-warm:#cdb48f;
  --band:#7d4137;
  --band-dark:#6a342c;
  --strip:#ffffff;
  --accent:#7fb21c;
  --text:#1f1f1f;
  --title:#ffffff;
  --subtitle:#f0b8b0;
  --footer:#7fb21c;
  --shadow:rgba(0,0,0,.28);
}
*{box-sizing:border-box;margin:0;padding:0}
html,body{width:1200px;height:1000px;overflow:hidden;background:var(--page)}
body{position:relative;font-family:"Carlito",Calibri,Arial,sans-serif;color:var(--text)}
h1,h2{font-weight:400}
.slide{position:absolute;width:562px;height:422px;overflow:hidden;box-shadow:2px 3px 6px var(--shadow);
  background:linear-gradient(90deg,var(--mat-mid),var(--mat-light) 30%,var(--mat-light) 70%,var(--mat-mid))}
.slide--cover{left:37px;top:54px}
.slide--meditation{left:622px;top:54px}
.slide--eating{left:37px;top:540px}
.slide--reflection{left:622px;top:540px}

.header-band{position:absolute;left:0;top:0;width:100%;height:66px;background:linear-gradient(90deg,var(--band-dark),var(--band))}
.header-strip{position:absolute;left:0;top:66px;width:100%;height:10px;background:var(--strip)}
.slide-title{position:absolute;left:17px;top:17px;font-size:25px;line-height:30px;color:var(--title)}

.logo-card{position:absolute;background:#fff;box-shadow:1px 2px 4px var(--shadow);border-top:7px solid var(--accent)}
.logo-card .logo-name{font-size:13px;font-weight:700;color:var(--band)}
.logo-card--small{left:432px;top:0;width:116px;height:100px}
.logo-card--small .logo-art{position:absolute;left:6px;top:4px;right:6px;bottom:4px;
  background:radial-gradient(ellipse at 60% 60%,#d9d2c8,#efebe5);display:flex;align-items:center;justify-content:center}

.cover-photo{position:absolute;left:0;top:0;width:100%;height:286px;background:linear-gradient(135deg,var(--mat-warm),#e8dac3 50%,var(--mat-warm))}
.cover-logo{position:absolute;left:350px;top:0;width:146px;height:209px;background:#fff;border-top:7px solid var(--accent)}
.cover-logo .logo-art{position:absolute;left:0;top:25px;width:100%;height:115px;background:radial-gradient(ellipse at 55% 55%,#d6cec3,#efebe5);
  display:flex;align-items:center;justify-content:center}
.cover-logo .logo-name{font-size:16px;font-weight:700;color:var(--band)}
.flower-bowl{position:absolute;left:478px;top:171px;width:56px;height:56px;border-radius:50%;background:radial-gradient(circle,#c9587e,#8a3a22 70%);border:3px solid #fff}
.cover-strip-top{position:absolute;left:0;top:286px;width:100%;height:10px;background:var(--strip)}
.cover-band{position:absolute;left:0;top:296px;width:100%;height:86px;background:linear-gradient(90deg,var(--band-dark),var(--band))}
.cover-strip-bottom{position:absolute;left:0;top:382px;width:100%;height:10px;background:var(--strip)}
.cover-base{position:absolute;left:0;top:392px;width:100%;height:30px;background:linear-gradient(90deg,var(--mat-warm),#e8dac3 50%,var(--mat-warm))}
.cover-title{position:absolute;left:12px;top:310px;font-size:25px;line-height:30px;color:var(--title)}
.cover-subtitle{position:absolute;left:12px;top:360px;font-size:15px;line-height:18px;color:var(--subtitle)}

.bullets{position:absolute;list-style:none;font-size:16px;line-height:19px;white-space:nowrap}
.bullets li{position:relative;padding-left:22px}
.bullets li::before{content:"";position:absolute;left:4px;top:7px;width:5px;height:5px;border-radius:50%;background:var(--accent)}
.bullets .sub{list-style:none;margin-top:3px;font-size:12.5px;line-height:17px}
.bullets .sub li{padding-left:50px;margin-top:6px}
.bullets .sub li:first-child{margin-top:0}
.bullets .sub li::before{left:44px;top:6px;width:4px;height:4px}

.bullets--meditation{left:16px;top:127px}
.bullets--meditation li + li{margin-top:59px}
.bullets--eating{left:15px;top:101px}
.bullets--eating > li + li{margin-top:18px}

.photo{position:absolute;border:5px solid #fff;box-shadow:1px 2px 5px var(--shadow)}
.photo--dusk{left:360px;top:117px;width:160px;height:234px;background:linear-gradient(180deg,#1d2d5c,#4a5f8f 60%,#9a8aa0 85%,#222 100%)}
.photo--dish{left:305px;top:145px;width:237px;height:182px;background:linear-gradient(160deg,#d9a873,#a5452f 55%,#6b2a20)}

.poem{position:absolute;left:60px;top:99px;width:446px;text-align:center;font-size:16px;line-height:22px}
.poem p + p{margin-top:22px}

.footer{position:absolute;left:0;bottom:3px;width:100%;height:14px;font-size:9px;line-height:14px;color:var(--footer)}
.footer .date{position:absolute;left:16px}
.footer .course{position:absolute;left:245px}
.footer .page{position:absolute;left:479px}
</style>
</head>
<body>

<section class="slide slide--cover">
  <div class="cover-photo" role="img" aria-label="Bamboo mat photo with leaves and a meditating figure"></div>
  <div class="cover-logo">
    <div class="logo-art"><span class="logo-name">Cocoa Calm</span></div>
  </div>
  <div class="flower-bowl" role="img" aria-label="Bowl with pink and white flowers"></div>
  <div class="cover-strip-top"></div>
  <div class="cover-band"></div>
  <div class="cover-strip-bottom"></div>
  <div class="cover-base"></div>
  <h1 class="cover-title">Meditation</h1>
  <p class="cover-subtitle">Cocoa Calm</p>
</section>

<section class="slide slide--meditation">
  <div class="header-band"></div>
  <div class="header-strip"></div>
  <h2 class="slide-title">Meditation</h2>
  <div class="logo-card logo-card--small"><div class="logo-art"><span class="logo-name">Cocoa Calm</span></div></div>
  <ul class="bullets bullets--meditation">
    <li>Meditation is the process of sitting still<br>and concentrating on the breath.</li>
    <li>Not about clearing your mind but being<br>aware of the thoughts.</li>
  </ul>
  <div class="photo photo--dusk" role="img" aria-label="Silhouette of a person meditating on a rock at dusk"></div>
  <div class="footer"><span class="date">11-08-2013</span><span class="course">Name of the course</span><span class="page">2</span></div>
</section>

<section class="slide slide--eating">
  <div class="header-band"></div>
  <div class="header-strip"></div>
  <h2 class="slide-title">Eating Mindfully</h2>
  <div class="logo-card logo-card--small"><div class="logo-art"><span class="logo-name">Cocoa Calm</span></div></div>
  <ul class="bullets bullets--eating">
    <li>Really sensing what you are<br>eating:
      <ul class="sub">
        <li>Where it came from</li>
        <li>All the processes it went through<br>to get to you</li>
      </ul>
    </li>
    <li>No distractions like TV, computers<br>or telephones. Just be with the<br>food.</li>
    <li>Gives us an opportunity to really<br>taste the food and appreciate it.</li>
  </ul>
  <div class="photo photo--dish" role="img" aria-label="Open sandwiches topped with beetroot, fish and dill"></div>
  <div class="footer"><span class="date">11-08-2013</span><span class="course">Name of the course</span><span class="page">4</span></div>
</section>

<section class="slide slide--reflection">
  <div class="header-band"></div>
  <div class="header-strip"></div>
  <h2 class="slide-title">Food Reflection</h2>
  <div class="logo-card logo-card--small"><div class="logo-art"><span class="logo-name">Cocoa Calm</span></div></div>
  <div class="poem">
    <p>With wise reflection I eat this food.<br>Not for play, not for intoxication.<br>Not for fattening, not for beatification.</p>
    <p>Only to maintain this body.<br>To stay alive and healthy.<br>To support this way of life.</p>
    <p>Thus I let go of unpleasant feelings,<br>And do not stir up new ones.<br>There by the process of life goes on,<br>Blameless, at ease and in peace.</p>
  </div>
  <div class="footer"><span class="date">11-08-2013</span><span class="course">Name of the course</span><span class="page">5</span></div>
</section>

</body>
</html>
```